Custom Framing Shop Stonebrook Framing Studio

I want an eye catching graphic that will be used a s business sign on a busy road. The sign MUST communicate the type of business it is clearly to vehicles traveling at 40 mph. This is a custom picture framing business and the sign will be hanging and be approximately 32" X 48". The business name is Stonebrook Framing Studio; Custom framing: by appointment and should include a whole or partial image of a picture frame as a visual que. I've included inspiration idea's, color pallets and styles that I like and a current business card for inspiration. I like the crimson font style shadowing and background colors of the attached Pello's pizzeria sign. I'd prefer crimson letters. Custom Framing is the message to communicate, followed by phone number and business name. I like the idea of a shield shape with a banner since it would more eye catching, Once again the Stonebrook image and name is less important than communicating what the business does. I like Crimson, grey, gold, black but am open to new ideas . I like the idea of a shield with a banner more than a rectangle, but am open to idea's

Target Market(s)

My target market is local homeowners ($700k+) who want a relationship with their framer and are willing to pay for a customized experience compared to a craft store experience. I have more female clients then men.

Industry/Entity Type

Picture Framing Art

Other font styles liked:
• Look at the attached image of a custom pizzeria sign, its kid of a custom car pinstripe font style. Script and decorative may be difficult to read while driving by but add to the elegance.

Colors

Designer to choose colors to be used in the design.

Requirements
Must have
• Clearly communicate what the business does "Custom framing" preferably with a picture frame and words
Nice to have
• incorporate a Stonebrook into the graphic
Should not have
• A Stonebrook image doesn't communicate what the business does to a vehicle traveling at 40 mph by the sign

```html
<!DOCTYPE html>
<html lang="en">
<head>
<meta charset="utf-8">
<title>Custom Framing – Stonebrook Framing Studio Sign</title>
<link href="https://fonts.googleapis.com/css2?family=Cinzel:wght@700;900&family=Yellowtail&display=swap" rel="stylesheet">
<style>
  :root {
    --backdrop-light: #f4f4f4;
    --backdrop-mid: #e2e2e2;
    --sign-border: #4a0508;
    --sign-panel: #880a0e;
    --sign-glow: #a8121a;
    --lettering: #ecd3d5;
    --lettering-shadow: #4d0306;
  }
  * { margin: 0; padding: 0; box-sizing: border-box; }
  html, body {
    width: 1200px;
    height: 564px;
    overflow: hidden;
  }
  body {
    background: radial-gradient(ellipse at 50% 45%, var(--backdrop-light) 0%, var(--backdrop-mid) 100%);
    position: relative;
  }
  .sign {
    position: absolute;
    left: 225px;
    top: 28px;
    width: 750px;
    height: 500px;
    box-shadow: 0 30px 28px -22px rgba(0,0,0,0.45);
  }
  .sign-art {
    display: block;
    width: 750px;
    height: 500px;
  }
  .script {
    font-family: "Yellowtail", cursive;
  }
  .script-face { fill: var(--lettering); }
  .script-shadow { fill: var(--lettering-shadow); }
  .roman {
    font-family: "Cinzel", serif;
    font-weight: 700;
    fill: var(--lettering);
  }
  .phone {
    font-family: "Cinzel", serif;
    font-weight: 900;
    fill: var(--lettering);
  }
  .brand-dot { fill: var(--lettering); }
</style>
</head>
<body>
  <div class="sign">
    <svg class="sign-art" viewBox="0 0 750 500" xmlns="http://www.w3.org/2000/svg">
      <defs>
        <radialGradient id="glow-right" cx="545" cy="165" r="240" gradientUnits="userSpaceOnUse">
          <stop offset="0" stop-color="#a8121a"/>
          <stop offset="1" stop-color="#880a0e"/>
        </radialGradient>
        <radialGradient id="glow-left" cx="167" cy="275" r="150" gradientUnits="userSpaceOnUse">
          <stop offset="0" stop-color="#a0101a" stop-opacity="0.9"/>
          <stop offset="1" stop-color="#a0101a" stop-opacity="0"/>
        </radialGradient>
      </defs>

      <rect class="sign-border" width="750" height="500" fill="#4a0508"/>
      <polygon class="sign-panel"
        points="68,31 678,31 678,70 718,70 718,435 678,435 678,473 68,473 68,435 28,435 28,70 68,70"
        fill="url(#glow-right)"/>
      <circle cx="167" cy="275" r="150" fill="url(#glow-left)" role="img" aria-label="Soft sunburst glow behind the lettering"/>

      <g class="script">
        <text class="script-shadow" x="78" y="203" font-size="118" textLength="340" lengthAdjust="spacingAndGlyphs" transform="rotate(-8 78 203)">Custom</text>
        <text class="script-face" x="82" y="198" font-size="118" textLength="340" lengthAdjust="spacingAndGlyphs" transform="rotate(-8 82 198)">Custom</text>
        <text class="script-shadow" x="258" y="267" font-size="124" textLength="410" lengthAdjust="spacingAndGlyphs" transform="rotate(-9 258 267)">Framing</text>
        <text class="script-face" x="262" y="262" font-size="124" textLength="410" lengthAdjust="spacingAndGlyphs" transform="rotate(-9 262 262)">Framing</text>
      </g>

      <g class="brand-mark">
        <circle class="brand-dot" cx="167" cy="252" r="26"/>
        <text class="roman" x="167" y="308" font-size="18" text-anchor="middle" textLength="104" lengthAdjust="spacingAndGlyphs">Stonebrook</text>
      </g>

      <g class="studio-name">
        <text class="roman" x="493" y="329" font-size="38" text-anchor="middle" textLength="222" lengthAdjust="spacingAndGlyphs">Stonebrook</text>
        <text class="roman" x="493" y="367" font-size="38" text-anchor="middle" textLength="344" lengthAdjust="spacingAndGlyphs">Framing Studio</text>
      </g>

      <text class="phone" x="375" y="457" font-size="66" text-anchor="middle" textLength="564" lengthAdjust="spacingAndGlyphs">(360) - 555 - 0148</text>
    </svg>
  </div>
</body>
</html>
```